Business Card Design for company

We want new business cards. We'd like something different-- yet still highly professional. Our tagline is Providing leadership, delivering success. Stock photos are ok, as long as they are relevant and look upscale.

Target Market(s)

Architecture/Business Management Consulting/Engineering Consulting

Contact Information for Business Card

dark gray background with pops of blue might be good, but you tell me. You're the designers. Rounded corners might be nice, but again, you tell me.

Font styles to use
Serif
Sans Serif

Colors
3276b5
5c5c5c
9d9d9d
fbfbfb

Requirements
Nice to have
• Something different, but still very professional.

```html
<!DOCTYPE html>
<html lang="en">
<head>
<meta charset="utf-8">
<title>Arden Advisory – Business Cards</title>
<link href="https://fonts.googleapis.com/css2?family=Montserrat:wght@500;600&family=Open+Sans:wght@400;600&display=swap" rel="stylesheet">
<style>
  :root {
    --blue: #3276b5;
    --gray-dark: #5c5c5c;
    --gray-light: #9d9d9d;
    --white: #fbfbfb;
    --card: #1c1c1d;
    --stage: #2a2a2b;
    --rule: #2e2e30;
  }
  * { margin: 0; padding: 0; box-sizing: border-box; }
  html, body { width: 1200px; height: 900px; overflow: hidden; background: var(--stage); }
  .stage {
    width: 1200px; height: 900px;
    display: flex; flex-direction: column; align-items: center; justify-content: center; gap: 56px;
  }
  .card {
    position: relative;
    width: 560px; height: 320px;
    background: var(--card);
    border-radius: 22px;
    box-shadow: 0 14px 30px rgba(0,0,0,.45);
    font-family: "Open Sans", Arial, sans-serif;
    color: var(--white);
  }
  /* front */
  .card-front .brand {
    position: absolute; left: 0; right: 0; top: 112px;
    text-align: center;
    font-family: "Montserrat", Arial, sans-serif; font-weight: 600;
    font-size: 40px; letter-spacing: 3px; text-transform: uppercase;
    color: var(--gray-light);
  }
  .card-front .tagline {
    position: absolute; left: 0; right: 0; bottom: 46px;
    text-align: center;
    font-family: "Montserrat", Arial, sans-serif; font-weight: 600;
    font-size: 15px; letter-spacing: .3px; text-transform: uppercase;
    color: var(--white);
  }
  /* back */
  .card-back .brand {
    position: absolute; right: 34px; top: 46px;
    font-family: "Montserrat", Arial, sans-serif; font-weight: 600;
    font-size: 30px; letter-spacing: 2px; text-transform: uppercase;
    color: var(--blue);
  }
  .card-back .divider {
    position: absolute; left: 30px; right: 30px; top: 128px;
    height: 1px; background: var(--rule);
  }
  .person { position: absolute; left: 34px; top: 168px; }
  .person .name {
    font-family: "Montserrat", Arial, sans-serif; font-weight: 600;
    font-size: 17px; text-transform: uppercase; letter-spacing: .4px;
    color: var(--blue);
  }
  .person .name .surname { color: var(--gray-dark); }
  .person .role { font-size: 13px; color: var(--white); margin-top: 1px; }
  .contacts { position: absolute; left: 34px; top: 222px; list-style: none; }
  .contacts li {
    display: flex; align-items: center; gap: 8px;
    font-size: 13.5px; line-height: 19px; color: var(--white);
  }
  .contacts svg { width: 12px; height: 12px; fill: var(--blue); flex: none; }
  .address {
    position: absolute; right: 34px; top: 190px;
    text-align: right; font-size: 13px; line-height: 19px; color: var(--white);
  }
</style>
</head>
<body>
<main class="stage">
  <section class="card card-front">
    <div class="brand">Arden Advisory</div>
    <p class="tagline">Providing leadership, delivering success</p>
  </section>

  <section class="card card-back">
    <div class="brand">Arden Advisory</div>
    <div class="divider"></div>
    <div class="person">
      <div class="name">Marcus <span class="surname">Hale</span></div>
      <div class="role">Managing Director</div>
    </div>
    <ul class="contacts">
      <li><svg viewBox="0 0 12 12" aria-hidden="true"><path d="M1 3.5C1 2 2.5 1.5 6 1.5S11 2 11 3.5V5H8.5V3.8H3.5V5H1Z M2.5 6h7l1 4.5h-9Z"/></svg>020-555 018 342</li>
      <li><svg viewBox="0 0 12 12" aria-hidden="true"><path d="M3.5 0.5h5a1 1 0 0 1 1 1v9a1 1 0 0 1-1 1h-5a1 1 0 0 1-1-1v-9a1 1 0 0 1 1-1Zm.5 1.5v7h4V2Z"/></svg>020-555 018 342</li>
      <li><svg viewBox="0 0 12 12" aria-hidden="true"><path d="M0.5 2.5h11v7h-11Zm1 1 4.5 3.2 4.5-3.2Z"/></svg>hello@ardenadvisory.com</li>
      <li><svg viewBox="0 0 12 12" aria-hidden="true"><circle cx="6" cy="6" r="5.5"/></svg>www.ardenadvisory.com</li>
    </ul>
    <address class="address" style="font-style:normal">48 , Harbour Row<br>Northbridge, 204518</address>
  </section>
</main>
</body>
</html>
```